Structural Engineering Business Card

Veltrow Drafts does residential house plans for clients in Central Florida. Would like simple but elegant business card that is appropriate for a house plan engineering company. Prefer black business card with black/white them but open to other shades of blue. I uploaded a sample card that I came across that looked good but please come up with your own creative designs.

Contact Information for Business Card

Name, Title, Phone, Email, Address, website

```html
<!DOCTYPE html>
<html lang="en">
<head>
<meta charset="utf-8">
<title>Veltrow Drafts — Business Card</title>
<link href="https://fonts.googleapis.com/css2?family=Montserrat:wght@400;500;800&family=Oswald:wght@500&display=swap" rel="stylesheet">
<style>
  :root {
    --backdrop: #1c1c1c;
    --card: #161616;
    --card-edge: #232323;
    --ink: #ffffff;
    --ink-soft: #e6e6e6;
  }
  * { margin: 0; padding: 0; box-sizing: border-box; }
  html, body { width: 1200px; height: 900px; overflow: hidden; }
  body {
    background: var(--backdrop);
    display: flex;
    flex-direction: column;
    align-items: center;
    justify-content: center;
    gap: 40px;
  }
  .card {
    width: 640px;
    height: 366px;
    background: linear-gradient(135deg, var(--card) 0%, #1d1d1d 60%, #252525 100%);
    border: 1px solid var(--card-edge);
    position: relative;
    box-shadow: 0 14px 30px rgba(0,0,0,.45);
  }
  .card--front {
    display: flex;
    align-items: center;
    justify-content: center;
  }
  .wordmark {
    display: flex;
    align-items: center;
    gap: 14px;
    color: var(--ink);
    font-family: "Montserrat", sans-serif;
    font-weight: 800;
    font-size: 40px;
    letter-spacing: 1px;
    text-transform: uppercase;
  }
  .wordmark__square {
    width: 26px;
    height: 26px;
    background: var(--ink);
  }
  .card--back {
    display: flex;
    align-items: center;
    padding-top: 70px;
  }
  .person {
    width: 295px;
    text-align: right;
    padding-right: 26px;
  }
  .person__name {
    font-family: "Oswald", sans-serif;
    font-weight: 500;
    font-size: 36px;
    line-height: 1.05;
    color: var(--ink);
    text-transform: uppercase;
  }
  .person__title {
    font-family: "Montserrat", sans-serif;
    font-size: 14px;
    letter-spacing: 1px;
    color: var(--ink-soft);
    text-transform: uppercase;
  }
  .divider {
    width: 1.5px;
    height: 120px;
    background: var(--ink-soft);
  }
  .contact {
    list-style: none;
    padding-left: 26px;
    font-family: "Montserrat", sans-serif;
    font-weight: 500;
    font-size: 15.5px;
    line-height: 1.45;
    color: var(--ink);
  }
  .contact li { display: flex; align-items: center; gap: 7px; }
  .contact svg { width: 12px; height: 12px; flex: none; }
  .contact .plain { padding-left: 19px; }
</style>
</head>
<body>
  <section class="card card--front">
    <div class="wordmark">
      <span class="wordmark__square"></span>
      <span>Veltrow Drafts</span>
    </div>
  </section>

  <section class="card card--back">
    <div class="person">
      <h1 class="person__name">Daniel Reyes</h1>
      <p class="person__title">Director</p>
    </div>
    <div class="divider"></div>
    <ul class="contact">
      <li class="plain">418 Marlow Lane</li>
      <li class="plain">Ocala, FL 34470</li>
      <li>
        <svg viewBox="0 0 24 24" fill="none" stroke="#fff" stroke-width="2.2"><path d="M5 3h4l2 5-2.5 1.5a11 11 0 0 0 6 6L16 13l5 2v4a2 2 0 0 1-2 2A16 16 0 0 1 3 5a2 2 0 0 1 2-2z"/></svg>
        352.555.0147
      </li>
      <li>
        <svg viewBox="0 0 24 24" fill="none" stroke="#fff" stroke-width="2.2"><rect x="3" y="5" width="18" height="14" rx="1"/><path d="M3 6l9 7 9-7"/></svg>
        info@veltrowdrafts.com
      </li>
      <li>
        <svg viewBox="0 0 24 24" fill="none" stroke="#fff" stroke-width="2"><circle cx="12" cy="12" r="9"/><path d="M3 12h18M12 3c3 3 3 15 0 18M12 3c-3 3-3 15 0 18"/></svg>
        www.veltrowdrafts.com
      </li>
    </ul>
  </section>
</body>
</html>
```